High Tech Real Estate Startup needs a business card

We are developing an innovative real estate marketing product based around advanced search and virtual reality.

We talk to people, we need business cards.

Target Market(s)

The target market is technology professionals and realtors.

Contact Information for Business Card

The information to be included will include

Name
Title
Phone Number
E-mail Address
www.plindo.com

It should use simple iconography for each one of those fields.

Font styles to use
Other font styles liked:
• Co, Jubilat, Avenir

Colors

Designer to choose colors to be used in the design.

Requirements
Must have
• Clean aesthetic,
• Good use of negative space.
• It should use our company logo, shown in the attached file. It is able to use the negative of that logo (coloured font and white background) and I have attached other acceptable accent colours in a swatch file.
Should not have
• Should not be too busy
• No extraneous text (slogans, tag lines etc)

```html
<!DOCTYPE html>
<html lang="en">
<head>
<meta charset="utf-8">
<title>Plindo Business Card</title>
<link href="https://fonts.googleapis.com/css2?family=Open+Sans:wght@400;600&display=swap" rel="stylesheet">
<style>
  :root {
    --teal: #10a9b1;
    --teal-dark: #0b8f96;
    --ink: #1b1b1b;
    --card: #ffffff;
    --card-shade: #eeeeee;
    --backdrop: #2e2f31;
  }
  html, body {
    margin: 0;
    padding: 0;
    width: 1200px;
    height: 900px;
    overflow: hidden;
    background: var(--backdrop);
    font-family: "Open Sans", Arial, sans-serif;
  }
  .business-card {
    position: absolute;
    left: 100px;
    top: 165px;
    width: 1000px;
    height: 570px;
    border-radius: 28px;
    overflow: hidden;
    background: radial-gradient(ellipse at 60% 35%, var(--card) 40%, var(--card-shade) 100%);
  }
  .swoosh {
    position: absolute;
    inset: 0;
    width: 100%;
    height: 100%;
  }
  .brand-name {
    position: absolute;
    left: 70px;
    top: 150px;
    margin: 0;
    font-size: 104px;
    font-weight: 600;
    letter-spacing: 4px;
    color: var(--teal);
    line-height: 1;
  }
  .divider {
    position: absolute;
    left: 555px;
    top: 110px;
    width: 2px;
    height: 290px;
    background: var(--teal);
  }
  .contact {
    position: absolute;
    left: 595px;
    top: 112px;
    color: var(--ink);
    font-size: 22px;
    line-height: 1.38;
  }
  .contact-name {
    margin: 0;
    font-size: 29px;
    font-weight: 600;
    color: var(--teal);
    letter-spacing: 0.5px;
  }
  .contact-title,
  .contact-address {
    margin: 0;
  }
  .contact-list {
    list-style: none;
    margin: 0;
    padding: 0;
  }
  .contact-list li {
    display: flex;
    align-items: center;
    gap: 10px;
  }
  .contact-icon {
    width: 16px;
    height: 16px;
    flex: none;
  }
</style>
</head>
<body>
  <div class="business-card">
    <svg class="swoosh" viewBox="0 0 1000 570" preserveAspectRatio="none" aria-hidden="true">
      <path d="M0,300 C170,440 500,540 800,570 L0,570 Z" fill="var(--teal)"/>
      <path d="M0,230 C190,400 500,515 800,548 C500,528 200,430 0,262 Z" fill="var(--ink)"/>
    </svg>

    <h1 class="brand-name">PLINDO</h1>
    <div class="divider"></div>

    <div class="contact">
      <p class="contact-name">DANIEL HARPER</p>
      <p class="contact-title">Director</p>
      <p class="contact-address">572 Maple Ridge Ln.<br>Franklin, TN 37064</p>
      <ul class="contact-list">
        <li>
          <svg class="contact-icon" viewBox="0 0 16 16" aria-hidden="true">
            <path d="M4 1.5 L6.5 4.5 L5 6.2 C6 8.3 7.7 10 9.8 11 L11.5 9.5 L14.5 12 L13 14.5 C7 14 2 9 1.5 3 Z" fill="var(--teal)"/>
          </svg>
          +1-615-555-0187
        </li>
        <li>
          <svg class="contact-icon" viewBox="0 0 16 16" aria-hidden="true">
            <rect x="1.5" y="3.5" width="13" height="9" fill="none" stroke="var(--teal)" stroke-width="1.5"/>
            <path d="M1.5 3.5 L8 9 L14.5 3.5" fill="none" stroke="var(--teal)" stroke-width="1.5"/>
          </svg>
          info@plindo.com
        </li>
        <li>
          <svg class="contact-icon" viewBox="0 0 16 16" aria-hidden="true">
            <circle cx="8" cy="8" r="6.5" fill="none" stroke="var(--teal)" stroke-width="1.5"/>
            <ellipse cx="8" cy="8" rx="2.8" ry="6.5" fill="none" stroke="var(--teal)" stroke-width="1.2"/>
            <path d="M1.5 8 H14.5" stroke="var(--teal)" stroke-width="1.2"/>
          </svg>
          www.plindo.com
        </li>
      </ul>
    </div>
  </div>
</body>
</html>
```